Business card for a boutique travel agency VELARIEN

we need a business card design - double sided. We would like to have a very elegant, sophisticated but modern design. we are travel consultants and our business focus is Europe, mainly the city of Paris. We would like to receive designs in white and silver, black color but if you are confident that we should pick up a color to make it different and more beautful...go ahead! We are going to give business cards to our clients and business partners. It is important to be perceived as elegant, modern and trustful. Please check jpg references.

Target Market(s)

Velarien primary clients are individuals, couples and affinity groups of high-net-worth who travel for leisure at least once per year. Seeking the ultimate travel experience, the target clients demand the finest quality activities and accommodations accompanied by a superior level of service.

Industry/Entity Type

Travel Industry

Contact Information for Business Card

Lucinda Farrow
- lucinda@velarien-example.com
- +55 11 98347.2516
- velarien-example.com
- unique travel experiences (we would like to see this signature printed as a detail)

Font styles to use
Sans Serif

Colors

Designer to choose colors to be used in the design.

Requirements
Must have
• the Velarien logo that I have attached
Nice to have
• we would like to have some nice detail, something different that shows that we care about,... we are detail oriented.
Should not have
• decorative fonts

```html
<!DOCTYPE html>
<html lang="en">
<head>
<meta charset="utf-8">
<title>Velarien Business Card</title>
<link rel="stylesheet" href="https://fonts.googleapis.com/css2?family=Jost:wght@300;400&family=Lato:wght@400&display=swap">
<style>
  :root {
    --backdrop: #cfcfcf;
    --card: #eae9e5;
    --ink: #1c1c1c;
    --ink-soft: #3a3a3a;
    --mark-faint: #d2d1cc;
    --silver: #b9b8b3;
    --silver-soft: #d9d8d3;
    --sheen-light: #f6f5f2;
    --sheen-mid: #e1e0dc;
  }
  * { box-sizing: border-box; margin: 0; padding: 0; }
  html, body {
    width: 1200px;
    height: 900px;
    overflow: hidden;
    background: var(--backdrop);
  }
  .canvas {
    position: relative;
    width: 1200px;
    height: 900px;
  }
  .card {
    position: absolute;
    left: 250px;
    width: 700px;
    height: 400px;
    background: var(--card);
    box-shadow: 0 6px 18px rgba(0, 0, 0, 0.18);
    overflow: hidden;
  }
  .card--back { top: 40px; }
  .card--front { top: 460px; }

  /* Back side */
  .back-wordmark {
    position: absolute;
    left: 48px;
    top: 42px;
    font-family: "Jost", sans-serif;
    font-weight: 300;
    font-size: 40px;
    letter-spacing: 0.42em;
    color: var(--mark-faint);
  }
  .contact {
    position: absolute;
    left: 64px;
    top: 210px;
  }
  .contact__name {
    font-family: "Jost", sans-serif;
    font-weight: 400;
    font-size: 22px;
    letter-spacing: 0.22em;
    text-transform: uppercase;
    color: var(--ink);
  }
  .contact__rule {
    width: 26px;
    height: 2px;
    background: var(--ink);
    margin: 14px 0 16px;
  }
  .contact__list {
    list-style: none;
    font-family: "Lato", sans-serif;
    font-size: 16px;
    line-height: 1.6;
    letter-spacing: 0.08em;
    color: var(--ink-soft);
  }
  .signature {
    position: absolute;
    right: 48px;
    bottom: 40px;
    font-family: "Jost", sans-serif;
    font-weight: 300;
    font-size: 13px;
    letter-spacing: 0.32em;
    text-transform: uppercase;
    color: var(--silver);
  }

  /* Front side */
  .front-pattern {
    position: absolute;
    inset: 0;
    background:
      radial-gradient(ellipse at 85% 90%, var(--sheen-light) 0%, rgba(246, 245, 242, 0) 55%),
      linear-gradient(120deg, var(--sheen-mid) 0%, var(--card) 45%, var(--sheen-light) 100%);
  }
  .front-frame {
    position: absolute;
    inset: 22px;
    border: 1px solid var(--silver-soft);
  }
  .front-brand {
    position: absolute;
    left: 0;
    right: 0;
    top: 50%;
    transform: translateY(-50%);
    display: flex;
    align-items: center;
    justify-content: center;
    gap: 22px;
  }
  .front-brand__dot {
    width: 14px;
    height: 14px;
    border: 1.5px solid var(--silver);
    border-radius: 50%;
  }
  .front-wordmark {
    font-family: "Jost", sans-serif;
    font-weight: 400;
    font-size: 40px;
    letter-spacing: 0.34em;
    margin-right: -0.34em;
    color: var(--ink);
  }
</style>
</head>
<body>
<main class="canvas">
  <section class="card card--back" aria-label="Card back">
    <div class="back-wordmark">VELARIEN</div>
    <div class="contact">
      <h1 class="contact__name">Lucinda Farrow</h1>
      <div class="contact__rule"></div>
      <ul class="contact__list">
        <li>Cell: +55 11 98347.2516</li>
        <li>Email: lucinda@velarien-example.com</li>
        <li>Web: velarien-example.com</li>
      </ul>
    </div>
    <p class="signature">unique travel experiences</p>
  </section>

  <section class="card card--front" aria-label="Card front">
    <div class="front-pattern" role="img" aria-label="Subtle silver embossed repeating pattern of small brand symbols covering the card"></div>
    <div class="front-frame"></div>
    <div class="front-brand">
      <span class="front-brand__dot"></span>
      <span class="front-wordmark">VELARIEN</span>
    </div>
  </section>
</main>
</body>
</html>
```